Bright Harbor Consulting

I need a business card design and for my consulting business. I provide outsourced CFO services for start-ups and high growth companies. I call my company Bright Harbor Co because building a company is similar to building a stone pathway, selecting each stone and planning several stones head in order to properly place them - all while keeping an eye on the final design and curve of the path. The underlying idea I want to express with my marketing images is that I'm someone that you can count on to help build your business and be there step by step to help. I'm not the old gray-haired CFO that many folks think of. :) I've included a one-page summery that I'm working on, it includes a summary of what I do. I've used a muted pathway and with greens in the header , and do like the green, but am open to other colors if they work well. Would like something that looks like a pathway, but a more abstract version instead of a picture.

```html
<!DOCTYPE html>
<html lang="en">
<head>
<meta charset="utf-8">
<title>Bright Harbor Co – Business Card</title>
<link rel="stylesheet" href="https://fonts.googleapis.com/css2?family=Carlito:wght@400;700&display=swap">
<style>
  :root {
    --brand-green: #4a883f;
    --text-green: #48843c;
    --paper: #ffffff;
    --mark-light: #f5f7f6;
    --card-shadow: rgba(0, 0, 0, 0.35);
  }
  * { margin: 0; padding: 0; box-sizing: border-box; }
  html, body {
    width: 999px;
    height: 1200px;
    overflow: hidden;
    background: var(--paper);
    font-family: "Carlito", "Calibri", sans-serif;
  }
  .canvas { position: relative; width: 999px; height: 1200px; }

  .card {
    position: absolute;
    left: 28px;
    width: 949px;
    box-shadow: 4px 5px 6px var(--card-shadow);
  }
  .card-front { top: 48px; height: 543px; background: var(--paper); }
  .card-back { top: 631px; height: 541px; background: var(--brand-green); }

  .front-band {
    position: absolute;
    left: 0; bottom: 0;
    width: 100%; height: 28px;
    background: var(--brand-green);
  }

  .brand { position: absolute; display: flex; align-items: center; }
  .brand-dot { border-radius: 50%; flex: none; }
  .brand-name { font-weight: 700; white-space: nowrap; }

  .brand-front { left: 31px; top: 54px; }
  .brand-front .brand-dot { width: 130px; height: 130px; background: var(--brand-green); margin-right: 41px; }
  .brand-front .brand-name { font-size: 58px; line-height: 56px; color: var(--text-green); }

  .brand-back { left: 178px; top: 180px; }
  .brand-back .brand-dot { width: 184px; height: 184px; background: var(--mark-light); margin-right: 48px; }
  .brand-back .brand-name { font-size: 80px; line-height: 86px; color: var(--mark-light); }

  .holder { position: absolute; left: 38px; top: 302px; color: var(--text-green); }
  .holder-name { font-size: 40px; font-weight: 700; line-height: 40px; }
  .holder-role { font-size: 28px; line-height: 30px; margin-top: 3px; }

  .address {
    position: absolute; left: 36px; top: 435px;
    display: flex; color: var(--text-green);
    font-size: 24px; line-height: 32px;
  }
  .address .icon { width: 26px; height: 42px; margin: 8px 20px 0 0; }

  .contact-list {
    position: absolute; left: 538px; top: 399px;
    list-style: none; color: var(--text-green);
    font-size: 24px; line-height: 32px;
  }
  .contact-list li { display: flex; align-items: center; }
  .contact-list .icon { width: 26px; height: 26px; margin-right: 26px; }
</style>
</head>
<body>
<div class="canvas">

  <section class="card card-front">
    <div class="brand brand-front">
      <span class="brand-dot"></span>
      <span class="brand-name">Bright Harbor<br>Co</span>
    </div>

    <div class="holder">
      <p class="holder-name">Name Title</p>
      <p class="holder-role">designation</p>
    </div>

    <div class="address">
      <svg class="icon" viewBox="0 0 26 42" aria-hidden="true">
        <path d="M13 0C5.8 0 0 5.6 0 12.6 0 21 13 42 13 42S26 21 26 12.6C26 5.6 20.2 0 13 0Z" fill="var(--text-green)"/>
        <circle cx="13" cy="12.5" r="5" fill="var(--paper)"/>
      </svg>
      <p>suit # 00, Lorem ipsum<br>Lorem Lorem ipsum</p>
    </div>

    <ul class="contact-list">
      <li>
        <svg class="icon" viewBox="0 0 26 26" aria-hidden="true">
          <path d="M6 2 9.5 7.5 7 10c1.5 3.5 5 7 8.5 8.5L18 16l5.5 3.5-1.5 4C20 25 16 24.5 11 20S1 9 2.5 4.5Z" fill="var(--text-green)"/>
          <path d="M15 2.5a9 9 0 0 1 8.5 8.5M15 6.5a5 5 0 0 1 4.5 4.5" fill="none" stroke="var(--text-green)" stroke-width="2" stroke-linecap="round"/>
        </svg>
        <span>555-014-2387</span>
      </li>
      <li>
        <svg class="icon" viewBox="0 0 26 26" aria-hidden="true">
          <path d="M1 11 13 3l12 8v13H1Z" fill="var(--text-green)"/>
          <path d="M1 11l12 8 12-8" fill="none" stroke="var(--paper)" stroke-width="1.6"/>
          <circle cx="13" cy="11" r="2.5" fill="var(--paper)"/>
        </svg>
        <span>mara@brightharborco.com</span>
      </li>
      <li>
        <svg class="icon" viewBox="0 0 26 26" aria-hidden="true">
          <g fill="none" stroke="var(--text-green)" stroke-width="1.6">
            <circle cx="13" cy="13" r="11"/>
            <ellipse cx="13" cy="13" rx="5" ry="11"/>
            <path d="M2 13h22M4 7.5h18M4 18.5h18M13 2v22"/>
          </g>
        </svg>
        <span>www.brightharborco.com</span>
      </li>
    </ul>

    <div class="front-band"></div>
  </section>

  <section class="card card-back">
    <div class="brand brand-back">
      <span class="brand-dot"></span>
      <span class="brand-name">Bright Harbor<br>Co</span>
    </div>
  </section>

</div>
</body>
</html>
```